Business Card Design Project

Hello,

We have just created our new COMPANY LOGO via Pixel Harbor and would not like to turn our attention to new Business Cards.

We are a printing company based in Singapore & Las Vegas. We specialize in blue-print printing for the Architectural, Engineering and Construction industries

The design should be simple, professional, clean and organized.

The Business Cards should "pop" when seen and will hopefully be something that makes you look twice.

We have two different Pan-tones that we use for our company, feel free to use them if you think they will work for your design?

Orange: PMS 021
Gray: PMS 431

I have attached our current logo for your use and reference which should obvious be on our business cards.

Considering we have two locations on different continents, we need business cards templates where the address details need to be interchangeable for each different location (total 2)

First one:
38 Merrow Lane #03-11 to #03-15
Singapore 528473
Tel : +65 6847-3920
Fax : +65 6843-7702

Second one:
2381 W. Tanfield Rd, Suite 204
Las Vegas, Nevada 89152
Tel : (702) 555-4137
Fax : (702) 555-4189

We would also like to list a few of our key services on the card. Here are a few examples to get you going.

Plan Printing & Plotting
Digital Colour Printing
Cadline Printing
Specialty Book Making
Scanning & Archiving
Collection & Delivey

This is the first time i have requested for business cards to be created so please let me know if you require any additional information.
Many Thanks,
Tobin
Updates

Project Deadline Extended
Reason: It took us longer than expected to finalize our Company Logo We look forward to receiving your designs.

Target Market(s)

Our Target Market is construction related people.
Construction
Architecture
Engineering

Industry/Entity Type

Printing

Font styles to use
Other font styles liked:
• Times New Roman

Colors
faa54b
ffffff

Requirements
Must have
• The business card must have our Company Logo (attached)
The font used must be Times New Roman
Should not have
• Playful images of print designs and/or logos

```html
<!DOCTYPE html>
<html lang="en">
<head>
<meta charset="utf-8">
<title>Halvern Reprographics – Business Card</title>
<link rel="stylesheet" href="https://fonts.googleapis.com/css2?family=Tinos:ital,wght@0,400;0,700;1,700&display=swap">
<style>
  :root {
    --backdrop: #8d4f26;
    --card-gray: #636a70;
    --brand-orange: #f0632f;
    --text-gray: #5f666c;
    --paper: #ffffff;
    --divider: #c9cdd0;
  }
  * { box-sizing: border-box; margin: 0; padding: 0; }
  html, body { width: 1200px; height: 800px; overflow: hidden; }
  body {
    background: var(--backdrop);
    font-family: "Tinos", "Times New Roman", serif;
    position: relative;
  }
  .card {
    position: absolute;
    left: 267px;
    width: 521px;
    box-shadow: 0 2px 6px rgba(0,0,0,0.25);
  }
  .card-back {
    top: 115px;
    height: 303px;
    background: var(--card-gray);
    color: var(--paper);
    display: flex;
    flex-direction: column;
    justify-content: center;
    align-items: center;
    gap: 9px;
    font-size: 14px;
    letter-spacing: 0.2px;
  }
  .service-line .sep { color: var(--brand-orange); margin: 0 3px; }
  .service-line .sep.light { color: var(--divider); }
  .card-front {
    top: 427px;
    height: 305px;
    background: var(--card-gray);
    overflow: hidden;
  }
  .brand-panel {
    height: 165px;
    background: var(--paper);
    text-align: center;
    padding-top: 52px;
  }
  .brand-name {
    color: var(--brand-orange);
    font-weight: 700;
    font-size: 34px;
    line-height: 1;
    letter-spacing: 0.5px;
  }
  .brand-tagline {
    margin-top: 14px;
    color: var(--text-gray);
    font-style: italic;
    font-weight: 700;
    font-size: 15px;
  }
  .accent-band {
    height: 12px;
    background: var(--brand-orange);
  }
  .contacts {
    display: flex;
    justify-content: center;
    gap: 22px;
    padding-top: 33px;
    color: var(--paper);
    font-size: 14px;
    line-height: 16px;
  }
  .office { display: flex; flex-direction: column; }
  .office-sg { align-items: flex-end; text-align: right; }
  .office-lv { align-items: flex-start; }
  .contact-row { display: flex; align-items: center; gap: 6px; }
  .icon { width: 11px; height: 11px; fill: var(--brand-orange); flex: none; }
</style>
</head>
<body>
  <svg width="0" height="0" style="position:absolute" aria-hidden="true">
    <symbol id="icon-phone" viewBox="0 0 24 24">
      <path d="M6.6 10.8a15.2 15.2 0 0 0 6.6 6.6l2.2-2.2a1 1 0 0 1 1-.25 11.4 11.4 0 0 0 3.6.57 1 1 0 0 1 1 1V20a1 1 0 0 1-1 1A17 17 0 0 1 3 4a1 1 0 0 1 1-1h3.5a1 1 0 0 1 1 1c0 1.25.2 2.45.57 3.57a1 1 0 0 1-.25 1z"/>
    </symbol>
    <symbol id="icon-fax" viewBox="0 0 24 24">
      <path d="M6 2h12v6H6z M3 9h18a1 1 0 0 1 1 1v8h-4v4H6v-4H2v-8a1 1 0 0 1 1-1z M8 15v5h8v-5z"/>
    </symbol>
  </svg>

  <section class="card card-back" aria-label="Card back: services">
    <p class="service-line">Plan Printing &amp; Plotting<span class="sep">|</span>Digital Colour Printing<span class="sep light">|</span>Cadline Printing</p>
    <p class="service-line">Specialty Book Making<span class="sep light">|</span>Scanning &amp; Archiving<span class="sep">|</span>Collection &amp; Delivery</p>
  </section>

  <section class="card card-front" aria-label="Card front: brand and contacts">
    <header class="brand-panel">
      <p class="brand-name">Halvern Reprographics</p>
      <p class="brand-tagline">A Member of the Halvern Group of Companies</p>
    </header>
    <div class="accent-band"></div>
    <div class="contacts">
      <address class="office office-sg" style="font-style:normal">
        <span>38 Merrow Lane #03-11 to #03-15</span>
        <span>Singapore 528473</span>
        <span class="contact-row">+65 6847-3920 <svg class="icon"><use href="#icon-phone"/></svg></span>
        <span class="contact-row">+65 6843-7702 <svg class="icon"><use href="#icon-fax"/></svg></span>
      </address>
      <address class="office office-lv" style="font-style:normal">
        <span>2381 W. Tanfield Rd, Suite 204</span>
        <span>Las Vegas, Nevada 89152</span>
        <span class="contact-row"><svg class="icon"><use href="#icon-phone"/></svg> (702) 555-4137</span>
        <span class="contact-row"><svg class="icon"><use href="#icon-fax"/></svg> (702) 555-4189</span>
      </address>
    </div>
  </section>
</body>
</html>
```